Heritage Hollow Business Cards

Require a business card design. <br/><br/>Needs to include logo (either round or long version) plus these details:<br/>Maya Torvel<br/>Heritage Hollow<br/>maya@quonbrook.com.au<br/>02 6481 7390<br/>PO Box Glenwarra NSW 2913<br/>www.heritagehollow.com.au<br/><br/>I need in an editable format so that I can create for multiple staff members. <br/><br/>

Target Market(s)

We are an online store selling renovation products to home owners are builders. Looking for a classic classy design.

Industry/Entity Type

Home And Garden

Contact Information for Business Card

Maya Torvel
Heritage Hollow
maya@quonbrook.com.au
02 6481 7390
PO Box Glenwarra NSW 2913
www.heritagehollow.com.au

Colors

Designer to choose colors to be used in the design.

Requirements
Must have
• Must include Logo.

```html
<!DOCTYPE html>
<html lang="en">
<head>
<meta charset="utf-8">
<title>Heritage Hollow — Business Cards</title>
<link rel="stylesheet" href="https://fonts.googleapis.com/css2?family=Montserrat:wght@400;500;600&display=swap">
<style>
  :root {
    --stage: #e4ded5;
    --card-light: #ffffff;
    --card-dark: #0b0d0f;
    --ink: #1e2226;
    --ink-soft: #3a3f44;
    --rule: #48615b;
    --accent: #35524b;
    --sketch-light: #d4d4d4;
    --sketch-dark: #6f7377;
    --emboss: #2a2d31;
  }
  * { margin: 0; padding: 0; box-sizing: border-box; }
  html, body { width: 1200px; height: 859px; overflow: hidden; }
  body {
    background: var(--stage);
    font-family: "Montserrat", Arial, sans-serif;
    position: relative;
  }
  .card {
    position: absolute;
    top: 289px;
    width: 500px;
    height: 285px;
    border-radius: 14px;
    overflow: hidden;
    box-shadow: 0 10px 22px rgba(0,0,0,.28);
  }
  .card--front { left: 60px; background: var(--card-light); color: var(--ink); }
  .card--back  { left: 639px; background: linear-gradient(150deg, #16191c 0%, var(--card-dark) 60%); }

  .brand-seal {
    position: absolute;
    left: 33px; top: 20px;
    width: 104px; height: 104px;
    border: 1.2px solid var(--ink-soft);
    border-radius: 50%;
    display: flex; align-items: center; justify-content: center;
    text-align: center;
    font-weight: 500;
    font-size: 13.5px;
    line-height: 1.15;
    color: var(--ink);
  }
  .holder-name {
    position: absolute;
    left: 24px; top: 130px;
    font-size: 22px; font-weight: 500;
    letter-spacing: .2px;
  }
  .name-rule {
    position: absolute;
    left: 24px; top: 163px;
    width: 452px; height: 1.5px;
    background: var(--rule);
  }
  .postal {
    position: absolute;
    left: 24px; top: 175px;
    font-size: 13px; line-height: 18px;
    color: var(--ink-soft);
  }
  .contact-list {
    position: absolute;
    left: 24px; top: 214px;
    list-style: none;
    font-size: 13px; line-height: 17.5px;
    color: var(--ink-soft);
  }
  .contact-list li { display: flex; align-items: center; gap: 7px; }
  .contact-list svg { width: 11px; height: 11px; flex: none; }

  .sketch { position: absolute; }
  .sketch--front { right: 0; bottom: 0; width: 140px; height: 121px; }
  .sketch--back  { left: 0; bottom: 0; width: 142px; height: 115px; }

  .brand-emboss {
    position: absolute;
    left: 152px; top: 43px;
    width: 196px; height: 196px;
    border: 1.5px solid var(--emboss);
    border-radius: 50%;
    display: flex; align-items: center; justify-content: center;
    text-align: center;
    font-weight: 500;
    font-size: 24px;
    line-height: 1.15;
    color: var(--emboss);
  }
</style>
</head>
<body>

  <section class="card card--front">
    <div class="brand-seal">Heritage<br>Hollow</div>

    <h1 class="holder-name">Maya Torvel</h1>
    <div class="name-rule"></div>

    <p class="postal">PO Box Glenwarra<br>NSW 2913</p>

    <ul class="contact-list">
      <li>
        <svg viewBox="0 0 12 12" aria-hidden="true"><circle cx="6" cy="6" r="5.2" fill="none" stroke="var(--accent)" stroke-width="1.1"/><path d="M4 3.6l1 1.2-.5.7c.5 1 1.1 1.6 2 2l.7-.5 1.2 1-.6.9c-2 0-3.9-1.9-4-4z" fill="var(--accent)"/></svg>
        02 6481 7390
      </li>
      <li>
        <svg viewBox="0 0 12 12" aria-hidden="true"><rect x="1" y="2.5" width="10" height="7" fill="none" stroke="var(--accent)" stroke-width="1.1"/><path d="M1 2.5l5 4 5-4" fill="none" stroke="var(--accent)" stroke-width="1.1"/></svg>
        maya@quonbrook.com.au
      </li>
      <li>
        <svg viewBox="0 0 12 12" aria-hidden="true"><circle cx="6" cy="6" r="5.2" fill="var(--accent)"/><path d="M1 6h10M6 .8c-2 2.8-2 7.6 0 10.4M6 .8c2 2.8 2 7.6 0 10.4" fill="none" stroke="#fff" stroke-width=".7"/></svg>
        www.heritagehollow.com.au
      </li>
    </ul>

    <svg class="sketch sketch--front" viewBox="0 0 140 121" role="img" aria-label="Hand-drawn sketch of a gabled roof corner">
      <polygon points="0,121 126,0 140,10 140,121" fill="var(--sketch-light)" opacity=".55"/>
    </svg>
  </section>

  <section class="card card--back">
    <div class="brand-emboss">Heritage<br>Hollow</div>

    <svg class="sketch sketch--back" viewBox="0 0 142 115" role="img" aria-label="Hand-drawn white sketch of a roof with chimney">
      <polygon points="0,0 142,105 142,115 0,115" fill="var(--sketch-dark)" opacity=".6"/>
    </svg>
  </section>

</body>
</html>
```